Business Card Design

I run an executive search and head hunting company.
My areas of business is within financial services and I cover, primarily sales and trading.

I am looking for a double sided, black business card and would like to keep the design fairly simple. Name to front and details on the reverse.

I would require a logo - some logo ideas.

*****Just some idea I am playing with - a white out halo over the "i" in Holloway.
A quill or feather somewhere within the layout. Above the Holloway Pierce & Tandy ? beneath it ? etc......

I have attached something I quite like but the whole creativity and layout is down to you. I am thinking to have the "&" in between Holloway Pierce & Tandy, maybe white out perhaps and may have it spot gloss uv'd when it comes to print.

I am pretty open minded though !

Target Market(s)

financial services - brokers and investment banking

Industry/Entity Type

Financial

Contact Information for Business Card

Holloway Pierce & Tandy
No 9 The Cloisters
52 Wexcombe Lane
Ashbury
Wessex
CM17 8RT

Telephone - + 44 (0)1599 639 805
Mobile -+ 44 (0) 7623 970 315
email - oliver@hollowaypiercetandy.co.uk
web - www.hollowaypiercetandy.co.uk

Oliver Tandy
Managing Director

Colors

Designer to choose colors to be used in the design.

Requirements
Should not have
• Finance - brokers investment banking.

```html
<!DOCTYPE html>
<html lang="en">
<head>
<meta charset="utf-8">
<title>Holloway Pierce &amp; Tandy — Business Card</title>
<link href="https://fonts.googleapis.com/css2?family=Bebas+Neue&family=PT+Sans:wght@400;700&display=swap" rel="stylesheet">
<style>
  :root {
    --page: #ffffff;
    --card: #1d1d1d;
    --card-edge: #2a2a2a;
    --ink: #a6a6a8;
    --ink-strong: #b2b2b4;
    --rule: #9a9a9c;
  }
  html, body {
    margin: 0;
    padding: 0;
    width: 1200px;
    height: 999px;
    overflow: hidden;
    background: var(--page);
  }
  .canvas {
    position: relative;
    width: 1200px;
    height: 999px;
  }
  .card {
    position: absolute;
    background: var(--card);
    border-radius: 22px;
    box-shadow: 0 0 0 1px var(--card-edge), 0 2px 4px rgba(0,0,0,0.35);
    overflow: hidden;
  }
  .card-front {
    left: 110px;
    top: 45px;
    width: 779px;
    height: 443px;
  }
  .card-back {
    left: 239px;
    top: 511px;
    width: 778px;
    height: 441px;
    font-family: "PT Sans", sans-serif;
    color: var(--ink);
  }
  .wordmark {
    position: absolute;
    left: 0;
    right: 0;
    top: 182px;
    margin: 0;
    text-align: center;
    font-family: "Bebas Neue", sans-serif;
    font-weight: 400;
    font-size: 74px;
    line-height: 1;
    letter-spacing: 0;
    color: var(--ink);
  }
  .holder {
    position: absolute;
    left: 36px;
    top: 40px;
  }
  .holder-name {
    margin: 0;
    font-weight: 700;
    font-size: 24px;
    line-height: 28px;
    color: var(--ink-strong);
  }
  .holder-title {
    margin: 0;
    font-size: 19px;
    line-height: 24px;
  }
  .address {
    position: absolute;
    right: 48px;
    top: 200px;
    margin: 0;
    text-align: right;
    font-style: normal;
    font-size: 19px;
    line-height: 26px;
  }
  .divider {
    position: absolute;
    left: 0;
    right: 0;
    top: 287px;
    height: 3px;
    background: var(--rule);
  }
  .contacts {
    position: absolute;
    right: 80px;
    top: 308px;
    margin: 0;
    padding: 0;
    list-style: none;
    text-align: right;
    font-size: 19px;
    line-height: 26px;
  }
</style>
</head>
<body>
<div class="canvas">
  <section class="card card-front" aria-label="Card front">
    <h1 class="wordmark">Holloway Pierce &amp; Tandy</h1>
  </section>

  <section class="card card-back" aria-label="Card back">
    <div class="holder">
      <p class="holder-name">Oliver Tandy</p>
      <p class="holder-title">Managing Director</p>
    </div>
    <address class="address">
      Holloway Pierce &amp; Tandy No 9<br>
      The Cloisters 52 Wexcombe Lane<br>
      Ashbury Wessex CM17 8RT
    </address>
    <div class="divider"></div>
    <ul class="contacts">
      <li>+ 44 (0)1599 639 805</li>
      <li>07623 970 315</li>
      <li>oliver@hollowaypiercetandy.co.uk</li>
      <li>www.hollowaypiercetandy.co.uk</li>
    </ul>
  </section>
</div>
</body>
</html>
```